Harborline Crest Insurance Services

we are a high end insurance agency we specialize on Auto | Home | Business | Life looking for something professional and luxuries at the same time. if you guys need anything else please let me know.

Auto | Home | Business | Life must be under logo on the back with black background.

i want the back part to be black with our gold logo on it.

Target Market(s)

Auto | Home | Business | Life

Industry/Entity Type

Insurance Broker

Contact Information for Business Card

My logo is gold so a black in the back would be nice.

Font styles to use
Serif

Colors
000000

Requirements
Must have
• Big logo on the back with black background.

```html
<!DOCTYPE html>
<html lang="en">
<head>
<meta charset="utf-8">
<title>Harborline Crest Insurance Services — Business Card</title>
<link rel="stylesheet" href="https://fonts.googleapis.com/css2?family=EB+Garamond:wght@400;500&display=swap">
<style>
  :root {
    --page: #ffffff;
    --card-dark: #1f1f1f;
    --card-mid: #262626;
    --card-light: #464646;
    --gold: #e3ab2c;
    --white: #ffffff;
    --emblem: #3a3a3a;
    --emblem-edge: #2c2c2c;
  }
  * { margin: 0; padding: 0; box-sizing: border-box; }
  html, body {
    width: 1200px;
    height: 1200px;
    overflow: hidden;
    background: var(--page);
    font-family: "EB Garamond", Georgia, serif;
  }
  .canvas {
    position: relative;
    width: 1200px;
    height: 1200px;
  }
  .card {
    position: absolute;
    overflow: hidden;
    background: linear-gradient(20deg, var(--card-light) 0%, var(--card-mid) 35%, var(--card-dark) 75%);
  }
  .card--front { left: 275px; top: 202px; width: 653px; height: 373px; }
  .card--back  { left: 272px; top: 625px; width: 658px; height: 376px; border-bottom: 2px solid #cfcfcf; }

  .brand {
    position: absolute;
    left: 0; right: 0;
    top: 128px;
    display: flex;
    align-items: center;
    justify-content: center;
    gap: 16px;
  }
  .brand__mark {
    width: 58px; height: 58px;
    border-radius: 50%;
    background: var(--gold);
    flex: none;
  }
  .brand__name {
    color: var(--gold);
    font-weight: 500;
    font-size: 34px;
    line-height: 1.0;
  }
  .brand__name span { display: block; }
  .services {
    position: absolute;
    left: 0; right: 0;
    top: 262px;
    text-align: center;
    color: var(--white);
    font-size: 23px;
    font-weight: 400;
  }

  .emblem {
    position: absolute;
    left: 340px; top: 30px;
    width: 470px; height: 470px;
    border-radius: 50%;
    background: radial-gradient(circle at 30% 30%, var(--emblem) 0%, var(--emblem-edge) 80%);
    box-shadow: 0 0 24px rgba(0,0,0,0.55);
  }
  .contact {
    position: absolute;
    left: 42px;
    top: 220px;
    color: var(--gold);
    font-size: 21px;
    line-height: 27px;
  }
  .contact__address { margin-top: 28px; }
</style>
</head>
<body>
  <main class="canvas">
    <section class="card card--front" aria-label="Card front">
      <div class="brand">
        <div class="brand__mark" aria-hidden="true"></div>
        <div class="brand__name"><span>Harborline Crest</span><span>Insurance Services</span></div>
      </div>
      <p class="services">Auto | Home | Business | Life</p>
    </section>

    <section class="card card--back" aria-label="Card back">
      <div class="emblem" aria-hidden="true"></div>
      <div class="contact">
        <p class="contact__phone">000 - 0000 - 000</p>
        <p class="contact__role">CEO / COMPANY</p>
        <p class="contact__address">ADRESS XXXX . XXX. NUMBER X</p>
      </div>
    </section>
  </main>
</body>
</html>
```